Accounting business needs a fridge magnet design

I need a business card size design to be used as a fridge magnet.
It will need to be vertical not horizontal and it will have my logo and the services I provide listed below it.
It needs to be pleasing to the eye and catch peoples attention.
I have uploaded my current business card as a reference.
It can look totally different though, i am open to new ideas.

It will need to say:

Specialising in:
*Small Business Taxation
*Company & Trust Returns
*Financial Statements
*Partnership Taxation
*BAS preparation/lodgement
*Capital Gains Tax
*Business Start Ups
*Business Structuring
*Tax Planning

```html
<!DOCTYPE html>
<html lang="en">
<head>
<meta charset="utf-8">
<title>Arden Tax – Fridge Magnet</title>
<link rel="stylesheet" href="https://fonts.googleapis.com/css2?family=Arimo:wght@400&family=Montserrat:wght@500&display=swap">
<style>
  :root {
    --backdrop: #414141;
    --charcoal: #262729;
    --paper: #f3f3f5;
    --accent-blue: #1aa3dd;
    --heading-blue: #1a5a9e;
    --text-dark: #2a2a2c;
    --white: #ffffff;
    --badge-blue: #1b5ea6;
    --badge-yellow: #f3d21b;
    --partner-blue: #15a7e0;
  }
  * { margin: 0; padding: 0; box-sizing: border-box; }
  html, body {
    width: 1096px; height: 1200px; overflow: hidden;
    background: var(--backdrop);
  }
  .magnet {
    position: absolute; left: 283px; top: 138px;
    width: 530px; height: 924px;
    border-radius: 30px; overflow: hidden;
    background: var(--paper);
  }
  .brand-panel {
    position: absolute; left: 0; top: 0; width: 100%; height: 381px;
    background: var(--charcoal);
  }
  .brand-mark {
    position: absolute; left: 190px; top: 68px;
    width: 148px; height: 148px;
    border: 4px solid var(--white); border-radius: 50%;
  }
  .brand-name {
    position: absolute; left: 0; top: 232px; width: 100%;
    text-align: center;
    font-family: "Montserrat", sans-serif; font-weight: 500;
    font-size: 46px; letter-spacing: 0.34em; text-indent: 0.34em;
    color: var(--white);
  }
  .rule {
    position: absolute; left: 0; width: 100%; height: 4px;
    background: var(--accent-blue);
  }
  .rule-top { top: 381px; }
  .rule-bottom { top: 868px; }
  .services {
    position: absolute; left: 55px; top: 432px;
    font-family: "Arimo", sans-serif;
  }
  .services-heading {
    font-size: 32px; font-weight: 400; color: var(--heading-blue);
    margin-bottom: 10px;
  }
  .service-list { list-style: none; }
  .service-list li {
    display: flex; align-items: center;
    height: 33.7px; font-size: 23px; color: var(--text-dark);
  }
  .tick { width: 22px; height: 22px; margin: 4px 12px 0 6px; flex: none; }
  .footer-band {
    position: absolute; left: 0; top: 872px; width: 100%; height: 52px;
    background: var(--charcoal);
  }
  .accreditation-badge {
    position: absolute; left: 120px; top: 829px;
    width: 138px; height: 60px; display: flex;
  }
  .accreditation-badge .half-blue { flex: 1.5; background: var(--badge-blue); }
  .accreditation-badge .half-yellow { flex: 1; background: var(--badge-yellow); }
  .partner-badge {
    position: absolute; left: 315px; top: 818px;
    width: 78px; height: 78px; border-radius: 50%;
    background: var(--partner-blue);
  }
</style>
</head>
<body>
  <main class="magnet">
    <header class="brand-panel">
      <div class="brand-mark"></div>
      <div class="brand-name">ARDEN TAX</div>
    </header>
    <div class="rule rule-top"></div>

    <section class="services">
      <h2 class="services-heading">Specialising in</h2>
      <ul class="service-list">
        <li><svg class="tick" viewBox="0 0 22 22"><circle cx="10" cy="12" r="8" fill="none" stroke="#1a5a9e" stroke-width="2.4"/><path d="M6 11.5l4 4 9-10" fill="none" stroke="#1a5a9e" stroke-width="2.6" stroke-linecap="round" stroke-linejoin="round"/></svg>Small Business Taxation</li>
        <li><svg class="tick" viewBox="0 0 22 22"><circle cx="10" cy="12" r="8" fill="none" stroke="#1a5a9e" stroke-width="2.4"/><path d="M6 11.5l4 4 9-10" fill="none" stroke="#1a5a9e" stroke-width="2.6" stroke-linecap="round" stroke-linejoin="round"/></svg>Company &amp; Trust Returns</li>
        <li><svg class="tick" viewBox="0 0 22 22"><circle cx="10" cy="12" r="8" fill="none" stroke="#1a5a9e" stroke-width="2.4"/><path d="M6 11.5l4 4 9-10" fill="none" stroke="#1a5a9e" stroke-width="2.6" stroke-linecap="round" stroke-linejoin="round"/></svg>Financial Statements</li>
        <li><svg class="tick" viewBox="0 0 22 22"><circle cx="10" cy="12" r="8" fill="none" stroke="#1a5a9e" stroke-width="2.4"/><path d="M6 11.5l4 4 9-10" fill="none" stroke="#1a5a9e" stroke-width="2.6" stroke-linecap="round" stroke-linejoin="round"/></svg>Partnership Taxation</li>
        <li><svg class="tick" viewBox="0 0 22 22"><circle cx="10" cy="12" r="8" fill="none" stroke="#1a5a9e" stroke-width="2.4"/><path d="M6 11.5l4 4 9-10" fill="none" stroke="#1a5a9e" stroke-width="2.6" stroke-linecap="round" stroke-linejoin="round"/></svg>BAS preparation/lodgement</li>
        <li><svg class="tick" viewBox="0 0 22 22"><circle cx="10" cy="12" r="8" fill="none" stroke="#1a5a9e" stroke-width="2.4"/><path d="M6 11.5l4 4 9-10" fill="none" stroke="#1a5a9e" stroke-width="2.6" stroke-linecap="round" stroke-linejoin="round"/></svg>Capital Gains Tax</li>
        <li><svg class="tick" viewBox="0 0 22 22"><circle cx="10" cy="12" r="8" fill="none" stroke="#1a5a9e" stroke-width="2.4"/><path d="M6 11.5l4 4 9-10" fill="none" stroke="#1a5a9e" stroke-width="2.6" stroke-linecap="round" stroke-linejoin="round"/></svg>Business Start Ups</li>
        <li><svg class="tick" viewBox="0 0 22 22"><circle cx="10" cy="12" r="8" fill="none" stroke="#1a5a9e" stroke-width="2.4"/><path d="M6 11.5l4 4 9-10" fill="none" stroke="#1a5a9e" stroke-width="2.6" stroke-linecap="round" stroke-linejoin="round"/></svg>Business Structuring</li>
        <li><svg class="tick" viewBox="0 0 22 22"><circle cx="10" cy="12" r="8" fill="none" stroke="#1a5a9e" stroke-width="2.4"/><path d="M6 11.5l4 4 9-10" fill="none" stroke="#1a5a9e" stroke-width="2.6" stroke-linecap="round" stroke-linejoin="round"/></svg>Tax Planning</li>
      </ul>
    </section>

    <div class="rule rule-bottom"></div>
    <footer class="footer-band"></footer>
    <div class="accreditation-badge" role="img" aria-label="Professional accreditation badge">
      <span class="half-blue"></span><span class="half-yellow"></span>
    </div>
    <div class="partner-badge" role="img" aria-label="Software partner badge"></div>
  </main>
</body>
</html>
```